Storm Restoration Contractor needs a professional business card design

Looking for a professional business card design. Not looking for your cheapo MS Word standard ones that are readily available. Dont want it to be cookie cutter look like ones readily available online. We just recently changed our logo and want to freshen up all our documents. Our company handles restoring a property back to a pre-loss condition after a storm damages it. For example, wind, hail, flood, fire losses.

Target Market(s)

Property Owners, Homeowners, Property Owners, Commercial Property Owners, Property Management Companies, Hail and Wind Damaged Properties

Industry/Entity Type

Construction Company

Contact Information for Business Card

Bramwell Outworks
555-418-7302
555-418-9047 fax
www.bramwelloutworks.example
info@bramwelloutworks.example

Requirements
Must have
• Clean, Professional, fresh look
• Storm Restoration, Roofing, Siding, Windows
Nice to have
• If there is a way to incorporate storms that may be cool.

```html
<!DOCTYPE html>
<html lang="en">
<head>
<meta charset="utf-8">
<title>Bramwell Outworks – Business Card</title>
<link rel="stylesheet" href="https://fonts.googleapis.com/css2?family=Lato:ital,wght@0,400;0,700;0,900;1,400&display=swap">
<style>
  :root {
    --blue: #1a7cc1;
    --charcoal: #58585a;
    --charcoal-dark: #4a4a4c;
    --text-grey: #4f4f51;
    --paper: #ffffff;
    --stage: #ececec;
  }
  * { margin: 0; padding: 0; box-sizing: border-box; }
  html, body { width: 1200px; height: 586px; overflow: hidden; }
  body {
    background: var(--stage);
    font-family: "Lato", Arial, sans-serif;
    position: relative;
  }
  .card {
    position: absolute;
    top: 128px;
    width: 502px;
    height: 302px;
    overflow: hidden;
  }
  .card--front { left: 65px; background: var(--charcoal); }
  .card--back { left: 608px; background: var(--paper); }

  /* brand lockup */
  .brand {
    position: absolute;
    left: 0; right: 0;
    display: flex;
    align-items: center;
    justify-content: center;
    gap: 12px;
  }
  .brand__dot {
    width: 72px; height: 72px;
    border-radius: 50%;
    border: 7px solid var(--blue);
    flex: none;
  }
  .brand__rule { width: 2px; height: 70px; background: var(--blue); flex: none; }
  .brand__name {
    font-weight: 900;
    font-size: 34px;
    line-height: 1.02;
    letter-spacing: 1px;
    text-transform: uppercase;
  }
  .card--front .brand { top: 92px; }
  .card--front .brand__name { color: var(--paper); }
  .card--back .brand { top: 38px; gap: 10px; }
  .card--back .brand__dot { width: 62px; height: 62px; border-width: 6px; }
  .card--back .brand__rule { height: 62px; }
  .card--back .brand__name { color: var(--blue); font-size: 28px; }

  .services {
    position: absolute;
    left: 0; right: 0; top: 256px;
    display: flex;
    justify-content: center;
    align-items: center;
    gap: 10px;
    color: var(--paper);
    font-weight: 700;
    font-size: 11.5px;
  }
  .services__sep { width: 4px; height: 4px; border-radius: 50%; background: var(--blue); }

  /* contact block */
  .contact-tab {
    position: absolute;
    left: 0; top: 162px;
    width: 39px; height: 112px;
    background: var(--blue);
    border-radius: 0 14px 14px 0;
  }
  .contact-tab svg { position: absolute; left: 12px; width: 14px; height: 14px; fill: var(--paper); }
  .contact-list {
    position: absolute;
    left: 49px; top: 173px;
    list-style: none;
    color: var(--text-grey);
    font-size: 11.5px;
  }
  .contact-list li { height: 25px; line-height: 18px; }

  .person {
    position: absolute;
    right: 30px; top: 197px;
    text-align: right;
  }
  .person__name { color: var(--blue); font-weight: 700; font-size: 18px; }
  .person__role { color: var(--text-grey); font-style: italic; font-size: 12px; margin-top: 2px; }

  .footer-band { position: absolute; left: 0; bottom: 0; width: 502px; height: 16px; }
</style>
</head>
<body>

<section class="card card--front" aria-label="Card front">
  <div class="brand">
    <span class="brand__dot"></span>
    <span class="brand__rule"></span>
    <span class="brand__name">Bramwell<br>Outworks</span>
  </div>
  <div class="services">
    <span>Roofing</span><span class="services__sep"></span>
    <span>Siding</span><span class="services__sep"></span>
    <span>Windows/Doors</span><span class="services__sep"></span>
    <span>Gutters</span>
  </div>
</section>

<section class="card card--back" aria-label="Card back">
  <div class="brand">
    <span class="brand__dot"></span>
    <span class="brand__rule"></span>
    <span class="brand__name">Bramwell<br>Outworks</span>
  </div>

  <div class="contact-tab">
    <svg style="top:12px" viewBox="0 0 16 16" aria-hidden="true"><path d="M1 5c0-2 3-3 7-3s7 1 7 3v1h-3V5H4v1H1zM4 7h8l2 7H2z"/></svg>
    <svg style="top:37px" viewBox="0 0 16 16" aria-hidden="true"><path d="M4 1h8v4H4zM1 6h14v6h-3v3H4v-3H1zM5 10v3h6v-3z"/></svg>
    <svg style="top:62px" viewBox="0 0 16 16" aria-hidden="true"><path d="M1 3h14v10H1zM2 4l6 5 6-5v1L8 10 2 5z" fill-rule="evenodd"/></svg>
    <svg style="top:87px" viewBox="0 0 16 16" aria-hidden="true"><path d="M6.5 9.5l3-3M7 4l2-2a3 3 0 0 1 5 5l-2 2M9 12l-2 2a3 3 0 0 1-5-5l2-2" stroke="#fff" stroke-width="1.8" fill="none" stroke-linecap="round"/></svg>
  </div>
  <ul class="contact-list">
    <li>555-418-7302</li>
    <li>555-418-9047</li>
    <li>info@bramwelloutworks.example</li>
    <li>www.bramwelloutworks.example</li>
  </ul>

  <div class="person">
    <div class="person__name">Declan Marrow</div>
    <div class="person__role">Owner / Founder</div>
  </div>

  <svg class="footer-band" viewBox="0 0 502 16" preserveAspectRatio="none" aria-hidden="true">
    <rect x="0" y="4" width="320" height="12" fill="var(--charcoal)"/>
    <path d="M302 16 C306 6 312 3 324 3 H502 V16 Z" fill="var(--paper)"/>
    <path d="M306 16 C310 8 316 0 328 0 H502 V16 Z" fill="var(--blue)"/>
  </svg>
</section>

</body>
</html>
```